Forex Trading Software Sales Page

We need header, footer, mid section and background design for our new website for a forex software that helps people make better decision in forex trading. Simple Sales Page. You can use test name "Meridel Sample Layout" on the design itself.

The new design must be blue tone, corporate, look expensive, show confidence and wealth. Please show us how you can improve our current design style by making something similar to the designed attached or making something entirely different that will better deliver the message to the visitors.

3 Examples of our previous designs are attached.

Target Market(s)

Forex Beginners, People who want to make money at home.

Industry/Entity Type

Business

Number of Pages Required

1 page

Font styles to use
Sans Serif

Colors
0255a3
eaf1f7
ffffff

Requirements
Must have
• The design must be 90% similar to this:
• https://www.quarnelbay7.com/
• 1) Name "Meridel Sample Layout" on header and footer.
• 2) PSDs of header, footer, mid section and background design.
• 3) Images of money bags, stacks etc
• 4) Show wealth, confidence and look expensive
• 5) Blueish tone of website mainly
• 6) Sample of headline and content colors and fonts.
Nice to have
• People will be buying products from this website, so it must not look too cheesy or over promising. Must give confidence and look expensive and clean.
Should not have
• Images of cars, yachts, villas or anything else that is associated with being rich.

```html
<!DOCTYPE html>
<html lang="en">
<head>
<meta charset="utf-8">
<title>Meridel Sample Layout – Order</title>
<link href="https://fonts.googleapis.com/css2?family=Roboto:wght@300;400;700&family=Roboto+Condensed:wght@300;400&family=Oswald:wght@300;500&display=swap" rel="stylesheet">
<style>
  :root{
    --brand-blue:#0255a3;
    --page-bg:#eaf1f7;
    --white:#ffffff;
    --gold:#e1a90f;
    --footer-bg:#1f1f21;
    --footer-text:#c9c9c9;
    --footer-muted:#7a7a7a;
    --title-blue:#1a5fb4;
  }
  *{margin:0;padding:0;box-sizing:border-box}
  html,body{width:1200px;height:750px;overflow:hidden}
  body{background:var(--page-bg);font-family:"Roboto",Arial,sans-serif;position:relative}

  .offer-band{position:absolute;left:0;top:0;width:1200px;height:378px;background:var(--page-bg)}
  .panel{position:absolute;top:0;height:336px;width:284px;background:var(--brand-blue);color:var(--white)}
  .panel--intro{left:150px}
  .panel--price{left:458px}
  .panel--guarantee{left:768px}

  .panel-copy{position:absolute;left:23px;top:-4px;width:245px;font-weight:300;font-size:12.8px;line-height:16.4px;letter-spacing:-0.1px}
  .panel-copy p{margin-bottom:16.4px}
  .panel--guarantee .panel-copy{top:-4px;width:240px}
  .panel--guarantee .panel-copy p{margin-bottom:16.4px}
  .panel--guarantee .panel-copy p.tight{margin-bottom:0}

  .scroll-cue{position:absolute;left:128px;top:307px}

  .price-label{position:absolute;top:5px;font-weight:300;font-size:17px}
  .price-label--regular{left:24px}
  .price-label--today{left:172px}
  .price-old{position:absolute;left:23px;top:24px;font-size:31px;font-weight:300;color:var(--gold);text-decoration:line-through;text-decoration-thickness:2px}
  .price-new{position:absolute;left:172px;top:21px;font-size:35px;font-weight:700;color:var(--gold)}
  .order-button{position:absolute;left:52px;top:86px;width:170px;height:36px;background:var(--gold);color:var(--white);font-weight:700;font-size:22px;display:flex;align-items:center;justify-content:center;letter-spacing:0.3px}

  .payment-methods{position:absolute;left:11px;top:161px;display:flex;gap:5.6px}
  .payment-methods span{width:48px;height:30px;background:#e9edf2;border-radius:2px;box-shadow:0 1px 2px rgba(0,0,0,.3)}
  .security-badge{position:absolute;top:234px;height:36px;border-radius:4px;background:rgba(255,255,255,.92)}
  .security-badge--one{left:17px;width:100px}
  .security-badge--two{left:140px;width:134px}

  .guarantee-seal{position:absolute;left:82px;top:182px}

  .site-footer{position:absolute;left:0;top:378px;width:1200px;height:372px;background:var(--footer-bg);text-align:center}
  .footer-title{position:absolute;left:0;width:100%;top:40px;font-family:"Oswald",sans-serif;font-weight:300;font-size:24px;color:var(--gold)}
  .footer-title strong{font-weight:500;color:var(--title-blue)}
  .footer-nav,.footer-notes{position:absolute;left:0;width:100%;font-family:"Roboto Condensed",sans-serif;font-size:12px;color:var(--footer-text);display:flex;justify-content:center}
  .footer-nav{top:89px}
  .footer-nav span{padding:0 25px}
  .footer-nav span.current{color:var(--white);font-weight:400}
  .footer-nav i,.footer-notes i{font-style:normal}
  .footer-notes{top:117px}
  .footer-notes span{padding:0 12px}
  .partner-mark{position:absolute;left:525px;top:168px;width:74px;height:74px;border-radius:8px;background:#5a5a5c}
  .owner-signature{position:absolute;left:528px;top:246px;width:190px;height:58px;background:linear-gradient(90deg,rgba(140,140,140,.15),rgba(140,140,140,.35),rgba(140,140,140,.15))}
  .copyright{position:absolute;left:0;width:100%;top:348px;font-weight:300;font-size:10.5px;color:var(--footer-muted)}
  .copyright b{font-weight:400;color:var(--white)}
</style>
</head>
<body>
  <section class="offer-band">
    <article class="panel panel--intro">
      <div class="panel-copy">
        <p>Tradeline Compass Pro is very easy to use. You get simple signals and alerts which tell you to buy or sell.</p>
        <p>It can't get easier than that. We wanted to make sure that you won't need any experi-ence to use it successfully.</p>
        <p>But nonetheless, if any questions arise, I will be more than happy to help you. I catch up with my emails every day, so it won't take long until you get a detailed reply from me.</p>
        <p>After you order, the system will automatically send you the download link to the indicator and user guide. The installation is super simple. It takes less than a minute. You will absolutely love it!</p>
      </div>
      <svg class="scroll-cue" width="26" height="14" viewBox="0 0 26 14" aria-hidden="true"><polyline points="1,1 13,12 25,1" fill="none" stroke="#fff" stroke-width="1.6"/></svg>
    </article>

    <article class="panel panel--price">
      <div class="price-label price-label--regular">Regular Price</div>
      <div class="price-label price-label--today">Today's Price</div>
      <div class="price-old">$147</div>
      <div class="price-new">$ 87</div>
      <div class="order-button">ORDER NOW</div>
      <div class="payment-methods" role="img" aria-label="Accepted payment methods">
        <span></span><span></span><span></span><span></span><span></span>
      </div>
      <div class="security-badge security-badge--one" role="img" aria-label="Security certificate badge"></div>
      <div class="security-badge security-badge--two" role="img" aria-label="Security certificate badge"></div>
    </article>

    <article class="panel panel--guarantee">
      <div class="panel-copy">
        <p>Dear Trader</p>
        <p class="tight">If for some weird reason at any time within the next 60 days you are not fully satisfied with the Tradeline Compass Pro, I will refund your order in FULL because I want you to feel safe. All the risk is on me here.</p>
        <p>You can give it an honest try for full 60 days with no questions, no hassles and no head-aches.</p>
      </div>
      <svg class="guarantee-seal" width="118" height="118" viewBox="0 0 118 118" role="img" aria-label="Satisfaction guarantee seal">
        <circle cx="59" cy="59" r="58" fill="#e6b02a"/>
        <circle cx="59" cy="59" r="44" fill="#f0c44a"/>
      </svg>
    </article>
  </section>

  <footer class="site-footer">
    <div class="footer-title"><strong>Meridel</strong> Sample Layout</div>
    <nav class="footer-nav">
      <span class="current">Home</span><i>|</i><span>About</span><i>|</i><span>Buy &amp; Sell</span><i>|</i><span>Benefits</span><i>|</i><span>FAQ</span>
    </nav>
    <div class="footer-notes">
      <span>24/7 Online Customer Support</span><i>|</i><span>One time payment</span><i>|</i><span>No hidden fees</span>
    </div>
    <div class="partner-mark" role="img" aria-label="Retail partner badge"></div>
    <div class="owner-signature" role="img" aria-label="Handwritten signature of the product owner"></div>
    <div class="copyright">© 2017 <b>Meridel Sample Layout</b>. All Right Reserved.</div>
  </footer>
</body>
</html>
```